Business Cards - New Logo Rebranding

Hello We know have a red and blue logo and are looking to create new cards. We are looking for the best creativity of the new logo merged with some of the existing artwork provided.

Target Market(s)

Realtors

Industry/Entity Type

Real Estate

Contact Information for Business Card

New logo with rebranded colors

Requirements
Must have
• Creative use of the new logo

```html
<!DOCTYPE html>
<html lang="en">
<head>
<meta charset="utf-8">
<title>Summit Group – Business Cards</title>
<link href="https://fonts.googleapis.com/css2?family=Russo+One&family=Oswald:wght@600&family=Open+Sans:wght@400;600&display=swap" rel="stylesheet">
<style>
  :root{
    --blue:#0b56a8;
    --blue-deep:#083f80;
    --blue-light:#1a6fc4;
    --red:#d9252f;
    --white:#ffffff;
    --paper:#f3f4f6;
    --ink:#3b3f45;
    --stage:#d9dbde;
  }
  *{box-sizing:border-box;margin:0;padding:0}
  html,body{width:1200px;height:900px;overflow:hidden;background:var(--stage)}
  .canvas{position:relative;width:1200px;height:900px}
  .card{position:absolute;top:150px;width:340px;height:600px;background:var(--paper);overflow:hidden;box-shadow:0 12px 30px rgba(0,0,0,.25)}
  .card--front{left:200px}
  .card--back{left:660px}
  .card svg.card-art{position:absolute;inset:0;width:340px;height:600px}
  .layer{position:absolute;left:0;width:100%;text-align:center}

  /* front */
  .brand{top:336px}
  .brand-name{font-family:"Russo One",sans-serif;font-size:34px;color:var(--blue);letter-spacing:1px;line-height:1}
  .brand-tag{font-family:"Open Sans",sans-serif;font-weight:600;font-size:10px;color:var(--red);letter-spacing:1.2px;margin-top:4px}
  .person{top:394px}
  .person-name{font-family:"Russo One",sans-serif;font-size:24px;letter-spacing:1px;line-height:1}
  .person-name .first{color:var(--blue)}
  .person-name .last{color:var(--red)}
  .person-title{font-family:"Open Sans",sans-serif;font-size:14px;color:var(--ink);margin-top:4px}
  .contact-icons{top:446px;display:flex;justify-content:center;gap:8px}
  .contact-icons svg{width:22px;height:22px}
  .contact-lines{top:473px;font-family:"Open Sans",sans-serif;font-size:13px;line-height:16px;color:var(--ink)}
  .contact-lines .hl{color:var(--blue)}
  .services{bottom:0;height:48px;line-height:48px;font-family:"Oswald",sans-serif;font-weight:600;font-size:13px;color:var(--white);letter-spacing:0;white-space:nowrap}

  /* back */
  .headline{top:24px;font-family:"Russo One",sans-serif;font-size:19px;color:var(--white);line-height:1.2;letter-spacing:.8px}
  .why{top:112px;left:28px;width:auto;text-align:left;font-family:"Russo One",sans-serif;font-size:15px;color:var(--red)}
  .reasons{position:absolute;top:144px;left:28px;right:18px;list-style:none;font-family:"Open Sans",sans-serif;font-size:13px;line-height:17px;color:var(--ink)}
  .reasons li{position:relative;padding-left:22px;margin-bottom:8px}
  .reasons li::before{content:"";position:absolute;left:0;top:2px;width:13px;height:13px;border-radius:50%;background:var(--blue);box-shadow:inset 0 -5px 0 var(--red)}
  .reasons sup{font-size:8px}
</style>
</head>
<body>
<div class="canvas">

  <!-- FRONT -->
  <section class="card card--front">
    <svg class="card-art" viewBox="0 0 340 600">
      <defs>
        <linearGradient id="frontBlue" x1="0" y1="0" x2="1" y2="1">
          <stop offset="0" stop-color="#1a6fc4"/>
          <stop offset="1" stop-color="#083f80"/>
        </linearGradient>
        <linearGradient id="portraitTone" x1="0" y1="0" x2="0" y2="1">
          <stop offset="0" stop-color="#8a96a8"/>
          <stop offset="1" stop-color="#1d4f9a"/>
        </linearGradient>
      </defs>
      <polygon points="0,0 340,0 340,205 225,250 0,305" fill="url(#frontBlue)"/>
      <g role="img" aria-label="Portrait photo of the inspector in a blue polo shirt">
        <polygon points="95,30 250,30 270,80 270,231 225,250 95,282 85,120" fill="url(#portraitTone)" opacity=".85"/>
      </g>
      <polyline points="0,305 225,250 340,205" fill="none" stroke="#d9252f" stroke-width="5"/>
      <circle cx="170" cy="283" r="42" fill="#d9252f"/>
      <rect x="0" y="552" width="340" height="48" fill="#0b56a8"/>
      <rect x="0" y="545" width="340" height="5" fill="#d9252f"/>
    </svg>

    <div class="layer brand">
      <div class="brand-name">SUMMIT GROUP</div>
      <div class="brand-tag">INSPECTION PROFESSIONALS</div>
    </div>

    <div class="layer person">
      <div class="person-name"><span class="first">DANIEL</span> <span class="last">REYES</span></div>
      <div class="person-title">Certified Mold Inspector</div>
    </div>

    <div class="layer contact-icons">
      <svg viewBox="0 0 24 24" aria-label="Office phone"><circle cx="12" cy="12" r="12" fill="var(--blue)"/><path d="M8 6l2 0 1 3-1.5 1a7 7 0 0 0 3.5 3.5l1-1.5 3 1 0 2a2 2 0 0 1-2 2A11 11 0 0 1 6 8a2 2 0 0 1 2-2z" fill="#fff"/></svg>
      <svg viewBox="0 0 24 24" aria-label="Mobile"><circle cx="12" cy="12" r="12" fill="var(--blue)"/><rect x="8.5" y="5" width="7" height="14" rx="1.5" fill="#fff"/><rect x="9.7" y="6.5" width="4.6" height="9" fill="var(--blue)"/></svg>
      <svg viewBox="0 0 24 24" aria-label="Email"><circle cx="12" cy="12" r="12" fill="var(--blue)"/><rect x="6" y="8" width="12" height="8" fill="#fff"/><path d="M6 8l6 5 6-5" fill="none" stroke="var(--blue)" stroke-width="1.2"/></svg>
      <svg viewBox="0 0 24 24" aria-label="Website"><circle cx="12" cy="12" r="12" fill="var(--blue)"/><g fill="none" stroke="#fff" stroke-width="1.2"><circle cx="12" cy="12" r="6"/><ellipse cx="12" cy="12" rx="2.6" ry="6"/><path d="M6 12h12M7 9h10M7 15h10"/></g></svg>
    </div>

    <div class="layer contact-lines">
      <div>800.555.0148</div>
      <div>562.555.0193</div>
      <div>dreyes@<span class="hl">summitinspect</span>.com</div>
      <div>www.<span class="hl">summitinspect</span>.com</div>
    </div>

    <div class="layer services">HOME • SEWER • MOLD • COMMERCIAL • TERMITE • ROOF</div>
  </section>

  <!-- BACK -->
  <section class="card card--back">
    <svg class="card-art" viewBox="0 0 340 600">
      <defs>
        <linearGradient id="backBlue" x1="0" y1="0" x2="1" y2="1">
          <stop offset="0" stop-color="#1a6fc4"/>
          <stop offset="1" stop-color="#083f80"/>
        </linearGradient>
      </defs>
      <rect width="340" height="600" fill="url(#backBlue)"/>
      <polygon points="0,108 130,82 340,82 340,440 230,482 0,482" fill="#f3f4f6"/>
      <polyline points="0,108 130,82 340,82" fill="none" stroke="#d9252f" stroke-width="4"/>
      <polyline points="340,440 230,482 0,482" fill="none" stroke="#d9252f" stroke-width="4"/>
      <g aria-label="Membership and certification badges">
        <circle cx="62" cy="452" r="22" fill="#c8202b" stroke="#fff" stroke-width="3"/>
        <circle cx="140" cy="448" r="22" fill="#1c3f7a" stroke="#c9a443" stroke-width="4"/>
        <circle cx="218" cy="440" r="22" fill="#9b9b8f" stroke="#d8d6c8" stroke-width="3"/>
        <rect x="50" y="520" width="110" height="38" rx="4" fill="#27367e" stroke="#c9a443" stroke-width="2"/>
        <circle cx="50" cy="539" r="21" fill="#2f4a8c" stroke="#c9a443" stroke-width="3"/>
        <rect x="200" y="512" width="56" height="22" rx="3" fill="#ffffff"/>
        <rect x="200" y="540" width="56" height="10" fill="#d9252f"/>
        <circle cx="292" cy="528" r="18" fill="#ffffff"/>
      </g>
    </svg>

    <div class="layer headline">CALIFORNIA'S #1<br>INSPECTION COMPANY!</div>
    <div class="layer why">WHY CHOOSE THE SUMMIT GROUP...</div>
    <ul class="reasons">
      <li>Performing Inspections Since 1984</li>
      <li>HomeCheck Guild Certified Master / Professional Inspectors<sup>®</sup></li>
      <li>500,000+ Inspections Completed Statewide</li>
      <li>Request of Repairs Pricer Report</li>
      <li>90-Day Inspection Guarantees</li>
      <li>Federally Licensed Drone Roof Inspectors upon request</li>
      <li>5,000+ 5-Star Reviews on Top Review Sites</li>
    </ul>
  </section>

</div>
</body>
</html>
```